Vantoro - where frequent flyers can cash out their airline miles

Vantoro enable the trade of airline miles between individuals. Our landing page which I want to redesign should refer to individuals who have miles in airline loyalty programs and would like to sell them with our platform

I would like to get a landing page design with a look and feel much more advanced and appealing then the one we currently have.

Page should include the information and fields in our current landing page but should be more professional and include except for the current two partner's logos and our logo of course, also the attached banner of staylark-example.com with a link to staylark-example.com with our affiliate code.

Audience of our web page is business men and heavy travellers therefore, page should reflect professionalism and should be business wise. There could be something that has to do with airplanes and money in terms of the background and pictures shows.

Additional text (on top of the short description at vantoro-example.com is -
"
Vantoro™ converts frequent flyers' accumulated miles to exceptionally low-priced flight tickets. It serves as an online trading platform for sellers of miles and buyers of flight tickets, offering airline customers a fully automated process whereby flight tickets are created out of loyalty club miles.
"

Our web site as a reference is www.vantoro-example.com

Target Market(s)

Business men who are heavily travellers

Industry/Entity Type

Travel Industry

Number of Pages Required

1 page

Font styles to use
Sans Serif

Colors
85acd3
0255a3

Requirements
Must have
• Our logo and the 3 logos mentioned at the description. It should have on the top the look & Feel that it currently has on our landing page - www.vantoro-example.com
Nice to have
• I would like people entering the web page to love it and for them to leave the relevant details so we get back to them
Should not have
• Not too many texts or images. Don't want people to scroll down too much if at all

```html
<!DOCTYPE html>
<html lang="en">
<head>
<meta charset="utf-8">
<title>Vantoro – Sell your miles</title>
<link href="https://fonts.googleapis.com/css2?family=Open+Sans:wght@400;600;700&display=swap" rel="stylesheet">
<style>
:root{
  --ink:#333;
  --muted:#555;
  --blue:#0a7fd0;
  --blue-dark:#0255a3;
  --blue-light:#85acd3;
  --line:#dcdcdc;
  --white:#fff;
}
*{box-sizing:border-box;margin:0;padding:0}
html,body{width:1200px;height:1077px;overflow:hidden;background:var(--white);font-family:"Open Sans",sans-serif;color:var(--ink)}
.page{position:relative;width:1200px;height:1077px}
.site-header{position:absolute;top:0;left:0;width:1200px;height:81px;background:var(--white)}
.brand{position:absolute;left:99px;top:22px;font-size:31px;font-weight:700;letter-spacing:1px;color:#111;line-height:1}
.main-nav{position:absolute;top:33px;right:99px;display:flex;gap:62px}
.main-nav a{font-size:12.5px;font-weight:600;color:#444;text-decoration:none;letter-spacing:.3px}
.hero{position:absolute;top:81px;left:0;width:1200px;height:594px;
  background:linear-gradient(160deg,#4a4f72 0%,#8a6c84 30%,#c88a84 55%,#b0707a 70%,#5a5676 100%)}
.hero-photo{position:absolute;inset:0;
  background:radial-gradient(ellipse at 78% 5%,rgba(240,210,170,.85),transparent 45%),
             radial-gradient(ellipse at 30% 40%,rgba(60,70,100,.55),transparent 55%),
             linear-gradient(180deg,transparent 60%,rgba(50,60,100,.6))}
.hero-intro{position:absolute;left:98px;top:412px;color:var(--white)}
.hero-intro h1{font-size:48px;font-weight:700;line-height:1}
.hero-intro p{font-size:16px;line-height:26.5px;margin-top:18px;width:450px}
.sell-form{position:absolute;left:632px;top:76px;width:470px;color:var(--white)}
.sell-form h2{font-size:48px;font-weight:400;line-height:1;letter-spacing:.5px}
.sell-form h3{font-size:20px;font-weight:400;margin-top:18px;margin-bottom:10px}
.sell-form h3.airlines{margin-top:22px}
.field-row{display:flex;gap:11px;margin-bottom:13px}
.field-row.tight{margin-bottom:11px}
.field{width:230px;height:35px;background:var(--white);border:1px solid #ddd;border-radius:2px;
  font:400 11.5px "Open Sans",sans-serif;color:#555;padding:0 15px;display:flex;align-items:center}
.btn{display:flex;align-items:center;justify-content:center;color:var(--white);font-weight:700;
  background:linear-gradient(#1a9be6,var(--blue) 60%,#0868b0);border:1px solid var(--blue-dark);border-radius:2px}
.btn-submit{width:230px;height:44px;font-size:17px;margin-top:3px}
.welcome{position:absolute;top:675px;left:0;width:1200px;height:299px}
.promo-banner{position:absolute;left:127px;top:37px;width:214px;height:214px;overflow:hidden;
  background:linear-gradient(180deg,#0c3d8e 0%,#1457a8 28%,#9fcde8 40%,#e8dcc4 58%,#4fb0d8 78%,#1d5f96 100%);color:var(--white);text-align:center}
.promo-title{font-size:16px;margin-top:10px}
.promo-sub{font-size:10.5px;margin-top:1px}
.promo-book{position:absolute;left:71px;top:152px;width:73px;height:26px;background:#1d8ff0;border:1px solid #fff;
  font-size:11.5px;display:flex;align-items:center;justify-content:center}
.promo-site{position:absolute;left:0;right:0;top:186px;font-size:12px;font-weight:700}
.welcome-text{position:absolute;left:398px;top:48px;width:640px}
.welcome-text h2{font-size:29px;font-weight:400;color:#555;line-height:1}
.welcome-text h2 strong{font-weight:700;color:#555}
.welcome-text p{font-size:13.3px;line-height:26.5px;color:#444;margin-top:10px;margin-left:3px;width:636px}
.btn-contact{position:absolute;left:2px;top:143px;width:145px;height:41px;font-size:15px}
.site-footer{position:absolute;top:974px;left:0;width:1200px;height:103px;border-top:1px solid var(--line)}
.footer-links{position:absolute;left:0;top:47px;width:590px;font-size:11px;color:#555}
.footer-links span{position:absolute;white-space:nowrap}
.social{position:absolute;left:598px;top:35px;display:flex;gap:9px}
.social span{width:34px;height:34px;border-radius:50%;display:block}
.s1{background:#2a63b8}.s2{background:#1d7aa6}.s3{background:#3bb0e6}.s4{background:#333}
.partner{position:absolute;top:43px;font-size:15px;font-weight:600;color:var(--muted)}
.partner.p1{left:855px}
.partner.p2{left:1010px}
</style>
</head>
<body>
<div class="page">
  <header class="site-header">
    <div class="brand">VANTORO</div>
    <nav class="main-nav">
      <a href="#">HOME</a><a href="#">ABOUT US</a><a href="#">CONTACT US</a>
    </nav>
  </header>

  <section class="hero">
    <div class="hero-photo" role="img" aria-label="Passenger jet flying over mountains at sunset"></div>
    <div class="hero-intro">
      <h1>Vantoro™</h1>
      <p>converts frequent flyers' accumulated miles to exception-ally low-priced flight tickets.</p>
    </div>
    <form class="sell-form">
      <h2>Sell your miles</h2>
      <h3>Personal Details</h3>
      <div class="field-row"><div class="field">First Name</div><div class="field">Last Name</div></div>
      <div class="field-row"><div class="field">Email</div><div class="field">Phone</div></div>
      <h3 class="airlines">Airlines Details</h3>
      <div class="field-row"><div class="field">Airline #1</div><div class="field">Amount of Miles</div></div>
      <div class="field-row tight"><div class="field">Airline #2</div><div class="field">Amount of Miles</div></div>
      <div class="field-row tight"><div class="field">Airline #3</div><div class="field">Amount of Miles</div></div>
      <div class="btn btn-submit">Submit now</div>
    </form>
  </section>

  <section class="welcome">
    <div class="promo-banner" role="img" aria-label="Beach resort with umbrellas and pool">
      <div class="promo-title">Vacation of a Lifetime</div>
      <div class="promo-sub">Book a slice of paradise</div>
      <div class="promo-book">Book now</div>
      <div class="promo-site">staylark-example.com</div>
    </div>
    <div class="welcome-text">
      <h2>Welcome to <strong>Vantoro™</strong></h2>
      <p>Vantoro™ converts frequent flyers' accumulated miles to exceptionally low-priced flight tickets. It serves as an online trading platform for sellers of miles and buyers of flight tickets, offering airline customers a fully automated process whereby flight tickets are created out of loyalty club miles. "</p>
      <div class="btn btn-contact">Contact now</div>
    </div>
  </section>

  <footer class="site-footer">
    <div class="footer-links">
      <span style="left:99px">Copyright © 2015. Vantoro™. All rights reserved.</span>
      <span style="left:363px">Terms &amp; Conditions</span>
      <span style="left:483px">/</span>
      <span style="left:505px">Privacy Policy</span>
    </div>
    <div class="social" aria-label="Social links">
      <span class="s1"></span><span class="s2"></span><span class="s3"></span><span class="s4"></span>
    </div>
    <div class="partner p1">Orvane</div>
    <div class="partner p2">Kestral</div>
  </footer>
</div>
</body>
</html>
```